New look and feel for investment website

Hi

Our website needs a crisp and professional look and feel applying to it. Here’s the address: http://www.brightplinth.co.uk. Since posting the brief yesterday (Tuesday, 16 August), we've reduced the amount of content on the home page, which should make life a little easier for you. We will come back later today, with some points of reference in terms of sites we like the look of. (See below)

17 August, 1.20pm GMT. OK, comments generally on the designs submitted so far. Please keep in mind that images of graphs, piles of coins, paper money and pretty females are not what is required. Better to think in terms of abstract imagery instead. Ratios? Circles? Relationships? Patterns? Not money,sex,graphs etc. Hope that helps.

For guidance on look and feel, please refer to these sites, which we like:

http://www.morvelle.co.uk/
http://www.qz.com/
https://www.harrowfieldtamsin.com
https://www.pirelconcerns.com
https://www.kvantule.com
Updates

Here's the Tall Beacons logo created in AI CS5.

Our market is professional financial advisers and relatively sophisticated private investors. The look and feel therefore should be slick and sophisticated - not 'lively' and lightweight, more like a banking site. Please read the brief again where we've added a list of websites that we really like the look of to get a better feel for what we're looking for. Thanks once again, we appreciate the work you're putting in.

It's essential that all the elements that are on the current home page be included on all new designs. 

We use a device in our e-mails which you may wish to incorporate in your design.

Target Market(s)

Professional financial advisers. People who know about investment and money.

Industry/Entity Type

Investment

Requirements
Should not have
• Graphs or people.

```html
<!DOCTYPE html>
<html lang="en">
<head>
<meta charset="utf-8">
<title>Tall Beacons – Home</title>
<link href="https://fonts.googleapis.com/css2?family=Open+Sans:wght@400;600&family=Arimo:wght@400;700&display=swap" rel="stylesheet">
<style>
:root{
  --page:#ebebeb;
  --card:#ffffff;
  --ink:#222222;
  --body:#444444;
  --muted:#555555;
  --slate:#5a6a80;
  --accent:#f0a030;
  --red:#e00000;
  --link:#1a5fb0;
  --rule:#d6d6d6;
  --box:#f7f7f7;
}
*{margin:0;padding:0;box-sizing:border-box}
html,body{width:811px;height:1200px;overflow:hidden;background:var(--page)}
body{position:relative;font-family:"Arimo",Arial,sans-serif;color:var(--body)}
.card{position:absolute;left:19px;top:18px;width:771px;height:1036px;background:var(--card);box-shadow:0 1px 4px rgba(0,0,0,.18)}
.brand{position:absolute;left:27px;top:26px;font-family:"Open Sans",sans-serif;font-weight:400;font-size:34px;line-height:40px;color:var(--ink)}
.top-nav{position:absolute;right:30px;top:38px;font-size:10px;color:var(--muted);letter-spacing:.2px}
.top-nav a{color:var(--muted);text-decoration:none}
.top-nav a.current{color:var(--accent)}
.top-nav .sep{margin:0 4px}
.hero{position:absolute;left:26px;top:83px;width:722px;height:280px;background:var(--slate);overflow:hidden}
.hero-art{position:absolute;left:0;top:0;width:400px;height:280px;background:radial-gradient(ellipse 60% 70% at 45% 50%,#f2f3f5 0%,#d9dde3 35%,#a9b2bf 65%,var(--slate) 100%)}
.hero-text{position:absolute;left:401px;top:63px;width:292px;font-family:"Open Sans",sans-serif;font-size:17.6px;line-height:21px;color:#fff}
.sub-nav{position:absolute;left:26px;top:373px;width:722px;height:24px;border-bottom:1px solid var(--rule);font-size:10px;color:var(--muted);padding-left:6px}
.sub-nav .sep{margin:0 5px;color:#aaa}
.sidebar{position:absolute;left:25px;top:422px;width:207px}
.reg-bar{height:40px;background:linear-gradient(#555,#111);color:#fff;font-family:"Open Sans",sans-serif;font-size:16px;line-height:40px;padding-left:13px;letter-spacing:.3px}
.reg-bar span{color:#f5c400}
.reg-copy{margin-top:9px;font-size:9.7px;line-height:14.6px;text-align:justify;color:var(--muted)}
.reg-copy strong{color:var(--ink)}
.reg-offer{margin-top:2px;font-size:9.7px;line-height:14.6px;color:var(--red);font-weight:700}
.click-btn{margin-top:7px;width:103px;height:28px;background:linear-gradient(#444,#0a0a0a);color:#fff;font-family:"Open Sans",sans-serif;font-size:14.5px;line-height:28px;padding-left:4px}
.click-btn span{color:#f5c400}
.stats{margin-top:14px;border:1px solid var(--rule)}
.stats li{list-style:none;padding:7px 10px 7px 9px;border-bottom:1px solid var(--rule);font-size:9.7px;line-height:14.6px;font-weight:700;color:var(--muted);background:var(--box)}
.stats li:last-child{border-bottom:none;padding-bottom:14px}
.main{position:absolute;left:246px;top:420px;width:510px}
.main h2{font-family:"Open Sans",sans-serif;font-weight:400;font-size:12.4px;color:var(--ink)}
.main p{font-size:9.3px;line-height:14.6px;text-align:justify;color:var(--body)}
.main .intro{margin-top:8px}
.main .lead{margin-top:12px;font-size:13.4px}
.point{padding-left:3px}
.point h3{margin-top:13px;margin-bottom:5px;font-size:9.3px;font-weight:700;color:var(--red)}
.point h3:first-child{margin-top:10px}
.main .more{margin-top:12px;font-family:"Open Sans",sans-serif;font-size:13.4px;line-height:20px;color:var(--ink);padding-left:3px;text-align:left}
.main .more a{color:var(--link);text-decoration:underline}
.main .more + .more{margin-top:4px}
.footer-note{position:absolute;left:19px;top:1068px;width:772px;font-size:9.3px;line-height:13px;font-weight:700;color:var(--ink)}
.legal{position:absolute;left:19px;top:1123px;width:772px;font-size:8.2px;line-height:11.4px;color:var(--muted);text-align:justify}
</style>
</head>
<body>
<div class="card">
  <div class="brand">Tall Beacons</div>
  <nav class="top-nav"><a class="current">Home</a><span class="sep">|</span><a>Login</a><span class="sep">|</span><a>Register for free</a><span class="sep">|</span><a>FAQs</a><span class="sep">|</span><a>Contact us</a><span class="sep">|</span><a>Terms &amp; Conditions</a></nav>

  <section class="hero">
    <div class="hero-art" role="img" aria-label="Abstract image of concentric ripples spreading across a grey surface"></div>
    <p class="hero-text">A potential return of 23.57 % a year from America’s biggest businesses with the emphasis firmly on capital preservation. (OK: we know you've yet to learn to love it, so that's why you can use our service free of charge for six months!)</p>
  </section>

  <nav class="sub-nav">Two Minute Guide<span class="sep">|</span>Current Portfolio<span class="sep">|</span>Watch list<span class="sep">|</span>Other key numbers<span class="sep">|</span>Back tested results<span class="sep">|</span>Trade History<span class="sep">|</span>Our analyses<span class="sep">|</span>Value investing<span class="sep">|</span>The Indices</nav>

  <aside class="sidebar">
    <div class="reg-bar">FREE REGISTRATION <span>›</span></div>
    <p class="reg-copy"><strong>We're not asking you to part company with any money — at least not right now.</strong> All we need from you at the moment is your e-mail address then you'll be able to view our portfolio and Watch list for 6 months free of charge!</p>
    <p class="reg-offer">Use our service FREE OF CHARGE for six months</p>
    <div class="click-btn">CLICK HERE <span>›</span></div>
    <ul class="stats">
      <li>Average, annualised compound return over to : 23.57 %</li>
      <li>So far this year, the portfolio's return is 13.49 %:</li>
      <li>Worst ever annual loss: -1.48 %; best ever annual gain: 69.77 %</li>
      <li>Average return per trade including losing trades: 24.44 %</li>
      <li>Maximum number of winning/losing trades in a row: 11/4.</li>
      <li>Average number of days a stock stays in the portfolio: 287</li>
      <li>An average of five trades a year and never more than five holdings at any one time.</li>
      <li>86 trades in total, of which 65 were profitable - a success rate of 75.58 %</li>
    </ul>
  </aside>

  <main class="main">
    <h2>Something different...</h2>
    <p class="intro">You may well be thinking that Tall Beacons is just another one of those banal share recommendation sites sprinkled with the usual idiotic and patronising platitudes, gross exaggerations, silly get-rich-quick promises and all the other stuff and nonsense you associate with the black art of share-tipping...</p>
    <h2 class="lead">Well, we have a pleasant surprise for you: you couldn't be further from the truth.</h2>
    <div class="point">
      <h3>No! No! No!</h3>
      <p>There's no newsletter to read, books to study, dvds to watch or traders' secrets to be revealed. No never-ending stream of recommendations. No webcasts. No effort or time to invest. No training. No research. No tedious market commentaries. And no financial discomfort for you whatsoever. (At least for the first six months that is!)</p>
      <h3>Undervalued and overlooked</h3>
      <p>Our program finds stocks that appear to be undervalued - i.e., where the price of a company's share does not reflect the real worth of the business. We confine our search to 1,000 of the USA's biggest companies; successful, robust, large cap businesses, which for one reason or another are either unpopular with investors or overlooked by them</p>
      <h3>We don't get it right every time...</h3>
      <p>We do however, get it right 75.58 % of the time (the total of all our winning trades out of all our trades) and on that basis tracking our portfolio should produce an average return of 23.57 % a year for you.</p>
      <h3>An average of five trades a year and never more than five holdings.</h3>
      <p>We tested different numbers of holdings and capital allocation percentages. The best results came from a portfolio of no more than five holdings with the same amount of capital allocated to each holding. That's it. You don't have to do it that way, but it works for us.</p>
    </div>
    <p class="more">For a succinct explanation of our service and the results to date...<a>please go here</a></p>
    <p class="more">» <a>More about the strategy we use to choose stocks... </a></p>
  </main>
</div>

<p class="footer-note">If you have any questions, please e-mail info@tallbeacons.co.uk. Although we’re very willing to answer queries about the way we pick stocks, please do keep in mind that as we’re giving this service away free of charge initially, we’re not inclined to expend time and energy debating the relative merits of value investing or fundamental analyses. Other than that, fire away!</p>
<p class="legal">This website is published by Tall Beacons Ltd. Registered in England No. 08417305. Registered office: 48 Fenwick Row London N7 2QD. This website and its content is the copyright of Tall Beacons Ltd - © Tall Beacons Ltd 2011. All rights reserved. Any redistribution or reproduction of part or all of the contents in any form is prohibited other than the following: you may print or download to a local hard disk extracts for your personal and non-commercial use only you may copy the content to individual third parties for their personal use, but only if you acknowledge the website as the source of the material. You may not, except with our express written permission, distribute or commercially exploit the content. Nor may you transmit it or store it in any other website or other form of electronic retrieval system.</p>
</body>
</html>
```